I'd like a business card that makes my company, Fenwright Marsh Associates Ltd stand out from the normal financial & IT services sector . It would be great to have a card that a potential client will think "wow" this is out of the norm , I'll give these guys a call. My business aims to provide consultancy services for financial and IT institutions but I'm looking to provide a newer approach that fits into today's social media rather than the standard "big 4" approach. My business helps companies assess their internal issues and aims to solve issues via business process re-engineering. The final design should have a balance of the maturity of the financial & IT sector with the fresh approach of the thriving social media sector

Target Market(s)

Business Managers and Directors, technical Managers and directors. Aged between 20 and 60 that handle project budgets

Industry/Entity Type

Financial

Requirements
Must have
• Must incorporate company logo currently being designed
Should not have
• No old-style fonts please.

```html
<!DOCTYPE html>
<html lang="en">
<head>
<meta charset="utf-8">
<title>Fenwright Marsh Associates – Business Card</title>
<link rel="stylesheet" href="https://fonts.googleapis.com/css2?family=Lato:wght@400;700&display=swap">
<style>
  :root {
    --canvas-bg: #ecedef;
    --card-blue: #1ba3df;
    --card-blue-light: #5fc4ee;
    --card-white: #fbfbfa;
    --ink-white: #ffffff;
    --ink-grey: #5a5b5d;
    --mark-blue: #3cb1e6;
    --card-shadow: 0 18px 40px rgba(40, 50, 60, 0.18);
  }
  * { box-sizing: border-box; margin: 0; padding: 0; }
  html, body {
    width: 1200px;
    height: 1000px;
    overflow: hidden;
    background: var(--canvas-bg);
    font-family: "Lato", sans-serif;
  }
  .card-set {
    position: absolute;
    inset: 0;
    display: flex;
    align-items: center;
    justify-content: center;
    gap: 64px;
  }
  .card {
    width: 520px;
    height: 316px;
    border-radius: 4px;
    box-shadow: var(--card-shadow);
    position: relative;
    overflow: hidden;
  }
  .card--front {
    background: radial-gradient(circle at 62% 70%, var(--card-blue-light) 0%, var(--card-blue) 62%);
    color: var(--ink-white);
    padding: 38px 40px 32px;
    display: flex;
    flex-direction: column;
  }
  .person-name {
    font-size: 19px;
    font-weight: 400;
    letter-spacing: 0.14em;
    text-transform: uppercase;
  }
  .person-role {
    font-size: 11px;
    letter-spacing: 0.04em;
    margin-top: 4px;
  }
  .contact-list {
    list-style: none;
    margin-top: 26px;
    font-size: 14px;
    line-height: 1.55;
  }
  .contact-label { margin-right: 6px; }
  .company-address {
    margin-top: auto;
    font-style: normal;
    font-size: 14px;
    line-height: 1.5;
  }
  .card--back {
    background: var(--card-white);
    display: flex;
    align-items: center;
    justify-content: center;
  }
  .brand-lockup {
    display: flex;
    align-items: center;
    gap: 18px;
  }
  .brand-dot {
    width: 46px;
    height: 46px;
    border-radius: 50%;
    background: var(--mark-blue);
  }
  .brand-name {
    font-size: 30px;
    font-weight: 400;
    letter-spacing: 0.08em;
    line-height: 1.05;
    text-transform: uppercase;
    color: var(--ink-grey);
  }
</style>
</head>
<body>
  <main class="card-set">
    <section class="card card--front" aria-label="Business card front">
      <h1 class="person-name">Alex Fenwright</h1>
      <p class="person-role">Managing Director</p>
      <ul class="contact-list">
        <li><span class="contact-label">mobile</span>07700 900461</li>
        <li><span class="contact-label">telephone</span>01632 960183</li>
        <li><span class="contact-label">email</span>alex@fenwrightmarsh.co.uk</li>
        <li><span class="contact-label">web</span>fenwrightmarsh.co.uk</li>
      </ul>
      <address class="company-address">
        Fenwright Marsh Associates Ltd<br>
        14 Alder Row&nbsp; Westby Green&nbsp; NE99 4QT
      </address>
    </section>

    <section class="card card--back" aria-label="Business card back">
      <div class="brand-lockup">
        <span class="brand-dot" aria-hidden="true"></span>
        <p class="brand-name">Fenwright<br>Marsh</p>
      </div>
    </section>
  </main>
</body>
</html>
```